Brennick Holdings Business Cards

These are professional business cards that are for my family office.
Put fake emails and phone numbers as of now until I finalize those components. This family office controls my families investments, assets, and future. The cards should be professional.
..
.
.
.
I just uploaded another variation of a logo I would like to see as a business card to I am inbeteen which logo to use

Target Market(s)

business

Industry/Entity Type

business

Contact Information for Business Card

Professional, wealth related, finance related.

Requirements
Must have
• Logo

```html
<!DOCTYPE html>
<html lang="en">
<head>
<meta charset="UTF-8">
<title>Brennick Holdings Business Cards</title>
<link rel="stylesheet" href="https://fonts.googleapis.com/css2?family=Playfair+Display:wght@400&family=Poppins:wght@400&display=swap">
<style>
  :root {
    --backdrop: #8a8a8a;
    --paper: #ffffff;
    --ink: #0a0a0a;
    --body-text: #2b2b2b;
    --gold: #c6b27a;
    --night: #000000;
    --rule: #9a9a9a;
  }
  * { box-sizing: border-box; margin: 0; padding: 0; }
  html, body {
    width: 1093px;
    height: 1200px;
    overflow: hidden;
    background: var(--backdrop);
  }
  .canvas {
    position: relative;
    width: 1093px;
    height: 1200px;
  }
  .card {
    position: absolute;
    left: 265px;
    width: 580px;
    height: 358px;
    border-radius: 24px;
    overflow: hidden;
  }
  .card--front { top: 226px; background: var(--paper); }
  .card--back { top: 622px; background: var(--night); }

  .wordmark {
    position: absolute;
    display: flex;
    align-items: center;
    gap: 10px;
    font-family: "Playfair Display", Georgia, serif;
    font-weight: 400;
    letter-spacing: 0.04em;
    white-space: nowrap;
  }
  .wordmark__square {
    display: block;
    background: var(--gold);
  }
  .card--front .wordmark {
    left: 28px;
    top: 188px;
    font-size: 21px;
    color: var(--ink);
  }
  .card--front .wordmark__square { width: 12px; height: 12px; }
  .card--back .wordmark {
    left: 0;
    right: 0;
    top: 156px;
    justify-content: center;
    font-size: 33px;
    color: var(--paper);
    gap: 16px;
  }
  .card--back .wordmark__square { width: 18px; height: 18px; }

  .divider {
    position: absolute;
    left: 288px;
    top: 74px;
    width: 1px;
    height: 210px;
    background: linear-gradient(to bottom, transparent, var(--rule) 20%, var(--rule) 80%, transparent);
  }

  .details {
    position: absolute;
    left: 310px;
    top: 92px;
    font-family: "Poppins", Arial, sans-serif;
    color: var(--body-text);
  }
  .details__name {
    font-family: "Playfair Display", Georgia, serif;
    font-size: 22px;
    line-height: 24px;
    color: var(--ink);
    letter-spacing: 0.01em;
    text-transform: uppercase;
  }
  .details__name-last { color: var(--gold); }
  .details__title {
    font-size: 16.5px;
    line-height: 20px;
    margin-top: -2px;
  }
  .contact-list {
    list-style: none;
    margin-top: 14px;
  }
  .contact-list__item {
    display: flex;
    align-items: center;
    gap: 7px;
    font-size: 16.5px;
    line-height: 21px;
  }
  .contact-list__icon { width: 16px; height: 16px; flex: none; }
  .details__address {
    font-style: normal;
    font-size: 16.5px;
    line-height: 21px;
    margin-top: 14px;
    margin-left: 1px;
  }
</style>
</head>
<body>
<main class="canvas">
  <section class="card card--front" aria-label="Business card front">
    <div class="wordmark"><span class="wordmark__square"></span>BRENNICK HOLDINGS</div>
    <div class="divider"></div>
    <div class="details">
      <p class="details__name">Edwin <span class="details__name-last">Harlow</span></p>
      <p class="details__title">Managing Director</p>
      <ul class="contact-list">
        <li class="contact-list__item">
          <svg class="contact-list__icon" viewBox="0 0 16 16" aria-hidden="true">
            <path d="M4 1.5l2.2 3-1.3 1.5c.8 1.9 2.2 3.3 4.1 4.1l1.5-1.3 3 2.2-1.3 2.3C7 13 3 9 1.7 2.8z" fill="none" stroke="#c6b27a" stroke-width="1.5" stroke-linejoin="round"/>
            <path d="M9.5 2.5a4.5 4.5 0 0 1 4 4M9.5 5a2 2 0 0 1 1.6 1.6" fill="none" stroke="#c6b27a" stroke-width="1.3" stroke-linecap="round"/>
          </svg>
          044-555 018 240
        </li>
        <li class="contact-list__item">
          <svg class="contact-list__icon" viewBox="0 0 16 16" aria-hidden="true">
            <rect x="0.5" y="3" width="15" height="10" fill="#c6b27a"/>
            <path d="M0.8 3.5L8 9l7.2-5.5" fill="none" stroke="#ffffff" stroke-width="1.2"/>
          </svg>
          info@brennickmail.com
        </li>
        <li class="contact-list__item">
          <svg class="contact-list__icon" viewBox="0 0 16 16" aria-hidden="true">
            <g fill="none" stroke="#c6b27a" stroke-width="1.2">
              <circle cx="8" cy="8" r="6.8"/>
              <ellipse cx="8" cy="8" rx="3" ry="6.8"/>
              <path d="M1.2 8h13.6M2.3 4.5h11.4M2.3 11.5h11.4"/>
            </g>
          </svg>
          www.brennickholdings.com
        </li>
      </ul>
      <address class="details__address">17 Larch Row, Suite 4<br>30918, Eastmere</address>
    </div>
  </section>

  <section class="card card--back" aria-label="Business card back">
    <div class="wordmark"><span class="wordmark__square"></span>BRENNICK HOLDINGS</div>
  </section>
</main>
</body>
</html>
```